Industrial Professional Business Card Design (Vantrel KX)

Would like professional looking business cards. Not too busy leaning towards minimal. Should have a slogan like:
"Industrial Automation and Control".

We are a tech company that programs industrial PLC computers. We also develop custom hardware solutions. Please use the logo for inspiration.

Target Market(s)

Mining, industrial, processing, automation, factory

Industry/Entity Type

Engineering

Contact Information for Business Card

Name, phone, email, website. job title.

Font styles to use
Other font styles liked:
• droid sans

Requirements
Must have
• Use colours that go well with the logo. Not too busy design.

```html
<!DOCTYPE html>
<html lang="en">
<head>
<meta charset="utf-8">
<title>Vantrel KX — Business Card</title>
<link href="https://fonts.googleapis.com/css2?family=Noto+Sans:wght@400;700&display=swap" rel="stylesheet">
<style>
  :root {
    --bg: #2a2a2a;
    --navy: #1b3f6e;
    --deep: #1e2a5c;
    --teal: #1f6f9c;
    --sky: #1aa6dc;
    --orange: #ef6a1f;
    --grey: #7a7a7a;
    --white: #ffffff;
  }
  * { box-sizing: border-box; margin: 0; padding: 0; }
  html, body { width: 1200px; height: 900px; overflow: hidden; }
  body {
    background: var(--bg);
    font-family: "Noto Sans", sans-serif;
    display: flex; flex-direction: column; align-items: center; justify-content: center;
    gap: 40px;
  }
  .card { width: 700px; height: 400px; position: relative; overflow: hidden; }

  /* back side */
  .card-back {
    background: var(--teal);
    display: flex; align-items: center; justify-content: center;
  }
  .back-texture {
    position: absolute; inset: 0;
    background: linear-gradient(120deg, #1d5884 0%, #1f6c98 55%, #1c6f9f 100%);
  }
  .back-brand {
    position: relative; display: flex; align-items: center; gap: 14px;
    color: var(--white); font-size: 40px; font-weight: 400; letter-spacing: 1px;
  }
  .brand-dot { width: 18px; height: 18px; border-radius: 50%; background: var(--orange); }

  /* front side */
  .card-front { background: var(--white); }
  .front-body {
    position: absolute; top: 0; left: 0; right: 0; height: 310px;
    display: flex; align-items: center;
  }
  .front-brand {
    width: 330px; display: flex; align-items: center; justify-content: center; gap: 12px;
    color: var(--navy); font-size: 40px; font-weight: 400; letter-spacing: 1px;
  }
  .divider { width: 2px; height: 150px; background: var(--orange); }
  .contact { padding-left: 44px; }
  .contact-name {
    font-size: 28px; font-weight: 700; letter-spacing: 2px; color: var(--navy);
  }
  .contact-role { font-size: 20px; color: var(--grey); margin-top: -2px; margin-bottom: 18px; }
  .contact-list { list-style: none; }
  .contact-list li {
    display: flex; align-items: center; gap: 14px;
    font-size: 20px; color: var(--grey); line-height: 1.5;
  }
  .contact-list svg { width: 18px; height: 18px; fill: var(--orange); flex: none; }
  .slogan-band {
    position: absolute; left: 0; right: 0; bottom: 40px; height: 44px;
    background: linear-gradient(90deg, var(--deep) 0%, #1f5b8c 35%, var(--sky) 75%, #2f55a8 100%);
    display: flex; align-items: center; padding-left: 170px;
    color: var(--white); font-size: 22px; letter-spacing: 1px; text-transform: uppercase;
  }
</style>
</head>
<body>
  <section class="card card-back">
    <div class="back-texture" role="img" aria-label="Faint repeating gear pattern in deep blue tones"></div>
    <div class="back-brand"><span class="brand-dot"></span>Vantrel KX</div>
  </section>

  <section class="card card-front">
    <div class="front-body">
      <div class="front-brand"><span class="brand-dot"></span>Vantrel KX</div>
      <div class="divider"></div>
      <div class="contact">
        <h1 class="contact-name">DARA HOLM</h1>
        <p class="contact-role">Sales Officer</p>
        <ul class="contact-list">
          <li><svg viewBox="0 0 24 24"><path d="M6.6 10.8a15 15 0 0 0 6.6 6.6l2.2-2.2c.3-.3.7-.4 1-.2 1.1.4 2.3.6 3.6.6.6 0 1 .4 1 1V20c0 .6-.4 1-1 1A17 17 0 0 1 3 4c0-.6.4-1 1-1h3.5c.6 0 1 .4 1 1 0 1.3.2 2.5.6 3.6.1.3 0 .7-.2 1z"/></svg>1-555-010-0142</li>
          <li><svg viewBox="0 0 24 24"><path d="M2 5h20v14H2zm2 2v.5l8 5 8-5V7zm0 2.8V17h16V9.8l-8 5z"/></svg>info@vantrelkx.com</li>
          <li><svg viewBox="0 0 24 24"><path d="M12 2a10 10 0 1 0 0 20 10 10 0 0 0 0-20zm6.9 9h-3a15 15 0 0 0-1.2-5.6A8 8 0 0 1 18.9 11zM12 4.1c.9 1.2 1.8 3.6 1.9 6.9h-3.8c.1-3.3 1-5.7 1.9-6.9zM9.3 5.4A15 15 0 0 0 8.1 11h-3a8 8 0 0 1 4.2-5.6zM5.1 13h3a15 15 0 0 0 1.2 5.6A8 8 0 0 1 5.1 13zm6.9 6.9c-.9-1.2-1.8-3.6-1.9-6.9h3.8c-.1 3.3-1 5.7-1.9 6.9zm2.7-1.3a15 15 0 0 0 1.2-5.6h3a8 8 0 0 1-4.2 5.6z"/></svg>www.vantrelkx.com</li>
        </ul>
      </div>
    </div>
    <div class="slogan-band">Industrial Automation and Control</div>
  </section>
</body>
</html>
```